Verpackungen für Matcha Tee Sticks
Zielgruppe
Premium Matcha Tee Sticks in hochwertiger Qualität. Die Umverpackung wird voraussichtlich in Dosen sein.
Unsere Zielgruppe sind Menschen mit Lust auf guten Geschmack und eine Prise Luxus, ReisSportler, Gesundheitsbewusste und Genießer.
Aufgabenstellung
Wir brauchen ein Logo & eine Verpackung (Banderole) für Dosen (Durchmesser: 63/ Höhe: 105 mm) für unser Label 'teefix4go'.
Modern, Luxuriös, Schlicht - Farben: gold, grün, schwarz, weiß (sind aber auch für andere Farbvarianten offen)
Die Matcha Sticks werden wahrscheinlich in schwarzen oder weißen oder goldenen Dosen verkauft werden.
Abmessungen Banderole: ca. Höhe: 105 / Breite:178mm
@all: Tendenziell sollen die Vorschläge noch luxuriöser und feiner werden. z.B. schwarzer Hintergrund mit feiner Schrift oder z.B. die Marke QRP Brew aus Singapur hat erlesene Tees in luxuriösem Design. Inspirierende Marken: Belnoix Vamont (Kekse, Kerzen), Ulla Verbeck (Kosmetik), Tissand Oulmes (Tee), Brevo oder ZAR Tee....
Es darf gerne ein Eyecatcher sein, IT-piece, must-have.... Eine Dose, die man lieber sammelt als nach Gebrauch wegzuschmeißen. Ihr könnt Euch auch vom Farbschema lösen. Das war nur ein erster Gedanke, da Matcha grün ist und die Dose voraussichtlich schwarz und gold Luxus verkörpert. Stellt Euch die Einkaufsmall in Dubai vor. Da heißt es auffallen. Knallorange....es muss rocken.
Wir sind gespannt auf weitere Vorschläge und möchten uns auch für die eingegangen Vorschläge bedanken. Wir wissen, dass da schon einiges an Arbeit drinsteckt.
Happy Weekend :)

```html
<!DOCTYPE html>
<html lang="de">
<head>
<meta charset="utf-8">
<title>teefix4go – Matcha Tee Sticks Banderole</title>
<link href="https://fonts.googleapis.com/css2?family=Cormorant+Garamond:wght@500&family=Great+Vibes&display=swap" rel="stylesheet">
<style>
  :root {
    --backdrop-light: #fbfbfd;
    --backdrop-edge: #d9dbe0;
    --label-black: #121212;
    --brand-gold: #b88a1c;
    --matcha-green: #8fb23c;
    --band-green: #8aa63a;
    --powder-dark: #6f8a2a;
    --powder-light: #a9c456;
    --text-white: #f2f2f2;
    --rule-grey: #8a8a8a;
    --band-text: #1a1a1a;
  }
  * { margin: 0; padding: 0; box-sizing: border-box; }
  html, body {
    width: 1153px;
    height: 1200px;
    overflow: hidden;
  }
  body {
    position: relative;
    background: radial-gradient(ellipse at 50% 45%, var(--backdrop-light) 0%, var(--backdrop-light) 40%, var(--backdrop-edge) 100%);
    font-family: "Cormorant Garamond", Georgia, serif;
  }
  .brand-mark {
    position: absolute;
    left: 136px;
    top: 590px;
    display: flex;
    align-items: center;
    gap: 12px;
    color: var(--brand-gold);
    font-size: 40px;
    font-weight: 500;
    letter-spacing: 0.5px;
  }
  .brand-dot {
    width: 14px;
    height: 14px;
    border-radius: 50%;
    background: var(--brand-gold);
  }
  .banderole {
    position: absolute;
    left: 589px;
    top: 160px;
    width: 316px;
    height: 836px;
    background: var(--label-black);
    overflow: hidden;
  }
  .banderole .brand-mark {
    position: absolute;
    left: 50%;
    top: 138px;
    transform: translateX(-50%);
    font-size: 28px;
    gap: 8px;
    white-space: nowrap;
  }
  .banderole .brand-dot { width: 10px; height: 10px; }
  .product-name {
    position: absolute;
    left: 0;
    right: 0;
    top: 340px;
    text-align: center;
    font-family: "Great Vibes", cursive;
    font-size: 96px;
    line-height: 1;
    color: var(--matcha-green);
  }
  .product-type {
    position: absolute;
    left: 0;
    right: 0;
    top: 438px;
    text-align: center;
    font-size: 48px;
    font-weight: 500;
    color: var(--text-white);
    letter-spacing: 1px;
  }
  .title-rule {
    position: absolute;
    left: 63px;
    top: 511px;
    width: 190px;
    height: 1px;
    background: linear-gradient(90deg, transparent, var(--rule-grey), transparent);
  }
  .powder-visual {
    position: absolute;
    left: 0;
    right: 0;
    top: 560px;
    height: 217px;
    background: radial-gradient(ellipse at 60% 85%, var(--powder-light) 0%, var(--powder-dark) 55%, var(--label-black) 100%);
  }
  .quality-band {
    position: absolute;
    left: 0;
    right: 0;
    top: 777px;
    height: 59px;
    background: var(--band-green);
    display: flex;
    align-items: center;
    justify-content: center;
    white-space: nowrap;
    font-size: 20px;
    font-weight: 500;
    color: var(--band-text);
  }
</style>
</head>
<body>
  <div class="brand-mark"><span class="brand-dot"></span>teefix4go</div>

  <section class="banderole">
    <div class="brand-mark"><span class="brand-dot"></span>teefix4go</div>
    <h1 class="product-name">Matcha</h1>
    <p class="product-type">Tee Sticks</p>
    <div class="title-rule"></div>
    <div class="powder-visual" role="img" aria-label="Heap of fine green matcha powder with scattered flakes"></div>
    <div class="quality-band">Premium Quality - Premium Quality - Premium</div>
  </section>
</body>
</html>
```